New Coffee Brand Packaging Design

We need a package design for our new coffee brand called Brindle Oak Coffee. Our brand mission will be displayed on the packaging (along the side or the back) and we currently have a logo that should be displayed on the front. Feel free to suggest a new logo design as you are designing the packaging if it doesn't fit with your vision. The final design should be creative and conservative. We like coffee colors (dark and light browns, white, cream, black, gold). We also like chalkboard art imagery (i.e. coffee cups, theme words from our mission, people, etc.). One famous person from West Louisville, KY is Terrence Vogt (world famous boxer and activist). If there is a way to draw his image in more of an abstract way where it doesn't infringe any patents that would be the sort of creativity we would like in the packaging. Our coffee brand prides itself on being a coffee for the people. For the average joe, working American who enjoys a good cup of coffee and a good atmosphere.

Brindle Oak Coffee Mission: "We aim to be a coffee company for the people. The people who have an appreciation and love for family, community and who never forget where they came from. Our coffee was born out of West Louisville, KY…a place like many others where the hearts, the minds and the wills are strong. We hope you enjoy each and every cup. Peace & Blessings."

Requirements
Must have
• (On the side or on the back of the packaging) Brindle Oak Coffee Mission: "We aim to be a coffee company for the people. The people who have an appreciation and love for family, community and who never forget where they came from. Our coffee was born out of West Louisville, KY…a place like many others where the hearts, the minds and the wills are strong. We hope you enjoy each and every cup. Peace & Blessings."
Nice to have
• Coffee Colors: dark and light browns, white, cream, black, gold

```html
<!DOCTYPE html>
<html lang="en">
<head>
<meta charset="utf-8">
<title>Brindle Oak Coffee – Packaging</title>
<link href="https://fonts.googleapis.com/css2?family=Oswald:wght@500&family=Tinos:ital,wght@0,400;0,700;1,400&display=swap" rel="stylesheet">
<style>
  :root {
    --page: #ffffff;
    --cream: #f6f1e7;
    --seal: #d9d3c9;
    --ink: #3a2a22;
    --espresso: #3b2419;
    --espresso-fold: #2a190f;
    --label: #4a3a33;
    --label-text: #f3ede4;
    --art: #8a7668;
  }
  * { margin: 0; padding: 0; box-sizing: border-box; }
  html, body { width: 1200px; height: 816px; overflow: hidden; background: var(--page); }
  .canvas { position: relative; width: 1200px; height: 816px; }

  .panel { position: absolute; top: 110px; height: 627px; }
  .panel--front, .panel--back {
    width: 321px;
    background: var(--cream);
    border-left: 9px solid var(--seal);
    border-right: 9px solid var(--seal);
  }
  .panel--front { left: 122px; }
  .panel--back { left: 768px; }
  .panel--side { left: 488px; width: 216px; background: var(--espresso); }
  .side-fold { position: absolute; left: 107px; top: 0; width: 2px; height: 100%; background: var(--espresso-fold); }

  .brand-vertical {
    position: absolute; left: 209px; top: 425px;
    transform: translate(-50%, -50%) rotate(-90deg);
    white-space: nowrap;
    font-family: "Tinos", serif; font-weight: 400; font-size: 30px;
    letter-spacing: 1px; color: var(--ink);
  }
  .hero-art {
    position: absolute; left: 269px; top: 273px; width: 125px; height: 177px;
    background: linear-gradient(180deg, #a28f81 0%, var(--art) 100%);
    border-radius: 4px;
  }
  .tagline {
    position: absolute; left: 271px; top: 452px; width: 134px;
    font-family: "Oswald", sans-serif; font-weight: 500; color: var(--ink);
    text-transform: uppercase; text-align: center; line-height: 1.15;
  }
  .tagline span { display: block; font-size: 19px; white-space: nowrap; }
  .tagline .tagline__big { font-size: 35px; letter-spacing: 4px; line-height: 1.05; }

  .info-box {
    position: absolute; left: 161px; top: 582px; width: 241px; height: 82px;
    background: var(--label); color: var(--label-text);
    font-family: "Tinos", serif; display: flex; padding: 8px 7px;
  }
  .info-box__col { flex: 1; }
  .info-box__col + .info-box__col { margin-left: 10px; padding-left: 6px; border-left: 1px solid var(--label-text); }
  .info-title { font-weight: 700; font-size: 12px; letter-spacing: 1px; padding-bottom: 2px; border-bottom: 1px solid var(--label-text); }
  .info-sub { font-size: 10px; padding: 2px 0 3px; border-bottom: 1px solid var(--label-text); margin-bottom: 3px; }
  .info-line { font-size: 7.5px; line-height: 1.25; }
  .info-line b { font-weight: 700; font-style: normal; }
  .info-line i { font-style: italic; }
  .info-rule { border-bottom: 1px solid var(--label-text); margin: 2px 0 4px; }
  .info-weight { font-size: 8.5px; font-weight: 700; }

  .mission { position: absolute; left: 822px; top: 367px; width: 230px; color: var(--ink); font-family: "Tinos", serif; }
  .mission__title { font-weight: 700; font-size: 11.5px; letter-spacing: 0.6px; margin-bottom: 18px; text-transform: uppercase; }
  .mission__body { font-size: 12.3px; line-height: 15.2px; }
  .brand-sign {
    position: absolute; left: 880px; top: 640px; width: 160px; text-align: right;
    font-family: "Tinos", serif; font-weight: 400; font-size: 17px; color: var(--ink);
  }
</style>
</head>
<body>
<main class="canvas">
  <section class="panel panel--front" aria-label="Front of bag"></section>
  <div class="brand-vertical">Brindle Oak Coffee</div>
  <div class="hero-art" role="img" aria-label="Chalk-style illustration of boxer Terrence Vogt with gloves raised"></div>
  <p class="tagline">
    <span>For the people</span>
    <span>who never forget</span>
    <span class="tagline__big">Where</span>
    <span>they came from</span>
  </p>
  <div class="info-box">
    <div class="info-box__col">
      <div class="info-title">COFFEE TYPE</div>
      <div class="info-sub">Smooth and Complex</div>
      <div class="info-line"><b>Aromas:</b> <i>Chocolate, Vanilla, Caramel, hints of Hazelnut &amp; Dark Berries</i></div>
    </div>
    <div class="info-box__col">
      <div class="info-line"><b>Roast:</b> Full City</div>
      <div class="info-rule"></div>
      <div class="info-line"><b>Brewing methods:</b></div>
      <div class="info-line"><i>Espresso, Pour Over, French Press, Aeropress</i></div>
      <div class="info-rule"></div>
      <div class="info-weight">12 OZ / 140g</div>
    </div>
  </div>

  <section class="panel panel--side" aria-label="Side gusset"><div class="side-fold"></div></section>

  <section class="panel panel--back" aria-label="Back of bag"></section>
  <div class="mission">
    <h2 class="mission__title">Brindle Oak Coffee Mission:</h2>
    <p class="mission__body">We aim to be a coffee company for the people.<br>The people who have an appreciation and love for family, community and who never forget where they came from.<br>Our coffee was born out of West Louisville, KY... a place like many others where the hearts, the minds and the wills are strong.<br>We hope you enjoy each and every cup.<br>Peace &amp; Blessings.</p>
  </div>
  <div class="brand-sign">Brindle Oak Coffee</div>
</main>
</body>
</html>
```